Korvex Systems*

Stationary design including business cards, letter heads, envelops and email signatures using our new logo

Target Market(s)

Innovative Technologies

Industry/Entity Type

Defense Contracting

Font styles to use
Sans Serif

```html
<!DOCTYPE html>
<html lang="en">
<head>
<meta charset="utf-8">
<title>Korvex Systems Stationery</title>
<link href="https://fonts.googleapis.com/css2?family=Encode+Sans+Condensed:wght@400&family=Lato:wght@400;700&family=Montserrat:wght@400;700&display=swap" rel="stylesheet">
<style>
  :root {
    --backdrop: #d9e4ef;
    --paper: #ffffff;
    --ink: #111111;
    --ink-soft: #555555;
    --ink-muted: #6f6f6f;
    --rule: #4a4a4a;
    --ghost: #eeeeee;
    --signature-tone: #e9e9e9;
  }
  * { box-sizing: border-box; margin: 0; padding: 0; }
  html, body { width: 1200px; height: 831px; overflow: hidden; }
  body {
    background: var(--backdrop);
    font-family: "Lato", sans-serif;
    color: var(--ink-soft);
    position: relative;
  }
  .sheet { position: absolute; background: var(--paper); }

  /* brand name lockup */
  .brand {
    position: absolute;
    display: flex;
    align-items: center;
    gap: 4px;
    font-family: "Montserrat", sans-serif;
    font-weight: 700;
    color: var(--ink);
    white-space: nowrap;
    text-transform: uppercase;
    letter-spacing: 0.02em;
  }
  .brand-square { background: var(--ink); flex: none; }

  /* letterhead */
  .letterhead { left: 117px; top: 111px; width: 430px; height: 609px; }
  .letterhead .brand { left: 40px; top: 94px; font-size: 13px; }
  .letterhead .brand-square { width: 8px; height: 8px; }
  .contact-block {
    position: absolute; right: 41px; top: 37px;
    text-align: right; font-size: 8px; line-height: 9.6px; color: var(--ink-muted);
  }
  .contact-block .address { margin-bottom: 4px; }
  .contact-line { display: flex; justify-content: flex-end; align-items: center; gap: 5px; height: 10.8px; }
  .contact-line svg { width: 7px; height: 7px; }
  .header-rule { position: absolute; left: 40px; top: 114px; width: 350px; height: 1px; background: var(--rule); }

  .letter-content { position: absolute; left: 40px; top: 190px; width: 350px; }
  .letter-date { font-family: "Montserrat", sans-serif; font-size: 9.5px; line-height: 12px; color: var(--ink-muted); }
  .recipient-name { margin-top: 5px; font-family: "Montserrat", sans-serif; font-weight: 700; font-size: 14.5px; line-height: 18px; color: var(--ink-soft); }
  .recipient-title { margin-top: 1px; font-family: "Montserrat", sans-serif; font-size: 9.5px; line-height: 12px; color: var(--ink-muted); }
  .letter-body {
    margin-top: 26px;
    font-family: "Encode Sans Condensed", sans-serif;
    font-size: 8.2px; line-height: 15px; color: var(--ink-soft);
  }
  .letter-body p { text-align: justify; margin-bottom: 15px; }
  .letter-body p:last-child { margin-bottom: 0; }
  .sign-off {
    margin-top: 29px;
    font-family: "Encode Sans Condensed", sans-serif;
    font-size: 9.5px; line-height: 12px; color: var(--ink-soft);
  }
  .signature-area { margin-top: 12px; margin-left: 1px; width: 45px; height: 30px; background: var(--signature-tone); }
  .footer-rule { position: absolute; left: 0; bottom: 14px; width: 100%; height: 1px; background: var(--rule); }
  .footer-band { position: absolute; left: 0; bottom: 0; width: 100%; height: 10px; background: var(--ink); }

  /* business cards */
  .card-front { left: 636px; top: 112px; width: 182px; height: 104px; }
  .card-front .brand { left: 10px; top: 66px; font-size: 5.8px; gap: 3px; letter-spacing: 0; }
  .card-front .brand-square { width: 4px; height: 4px; }
  .card-divider { position: absolute; left: 88px; top: 28px; width: 1px; height: 50px; background: var(--ink); }
  .card-details { position: absolute; left: 100px; top: 26px; color: var(--ink-muted); }
  .card-name { font-family: "Montserrat", sans-serif; font-weight: 700; font-size: 7.6px; color: var(--ink); }
  .card-role { font-size: 4.6px; margin-bottom: 5px; }
  .card-address { font-size: 4.4px; line-height: 5.6px; margin-bottom: 4px; }
  .card-contact { display: flex; align-items: center; gap: 3px; font-size: 4.4px; height: 6.6px; }
  .card-contact svg { width: 4px; height: 4px; }
  .card-back { left: 904px; top: 111px; width: 183px; height: 104px; }
  .card-back .brand { left: 50%; top: 63px; transform: translateX(-50%); font-size: 7px; }
  .card-back .brand-square { width: 5px; height: 5px; }

  /* envelopes */
  .envelope-back { left: 636px; top: 248px; width: 451px; height: 225px; }
  .envelope-flap { position: absolute; left: 0; top: 0; width: 451px; height: 67px; }
  .envelope-back .brand { left: 50%; top: 28px; transform: translateX(-50%); font-size: 7px; }
  .envelope-back .brand-square { width: 5px; height: 5px; }
  .envelope-front { left: 636px; top: 494px; width: 451px; height: 226px; }
  .envelope-front .brand { left: 40px; top: 90px; font-size: 13px; }
  .envelope-front .brand-square { width: 8px; height: 8px; }
  .brand-ghost {
    position: absolute; right: 44px; top: 104px;
    font-family: "Montserrat", sans-serif; font-weight: 700; font-size: 14px;
    text-transform: uppercase; color: var(--ghost); white-space: nowrap;
  }
  .return-address { position: absolute; left: 41px; top: 182px; font-size: 8px; line-height: 9.6px; color: var(--ink-muted); }
</style>
</head>
<body>

<section class="sheet letterhead">
  <div class="brand"><span class="brand-square"></span>Korvex Systems</div>
  <div class="contact-block">
    <div class="address">1234 First Line Address<br>5678 Second Line Address</div>
    <div class="contact-line">(555) 014-2290
      <svg viewBox="0 0 10 10"><path d="M2 1 L4 1 L4.6 3.2 L3.4 4.2 Q4.5 6 5.8 6.6 L6.8 5.4 L9 6 L9 8 Q8.5 9 7.5 9 Q1 8 1 2.5 Q1 1.5 2 1 Z" fill="var(--ink)"/></svg></div>
    <div class="contact-line">contact@korvexsystems.com
      <svg viewBox="0 0 10 10"><rect x="0.5" y="2" width="9" height="6.5" fill="var(--ink)"/><path d="M0.8 2.3 L5 5.8 L9.2 2.3" stroke="#fff" stroke-width="0.8" fill="none"/></svg></div>
    <div class="contact-line">www.korvexsystems.com
      <svg viewBox="0 0 10 10"><circle cx="5" cy="5" r="4.2" fill="none" stroke="var(--ink)" stroke-width="1"/><ellipse cx="5" cy="5" rx="1.8" ry="4.2" fill="none" stroke="var(--ink)" stroke-width="0.8"/><path d="M0.8 5 H9.2 M1.5 3 H8.5 M1.5 7 H8.5" stroke="var(--ink)" stroke-width="0.7"/></svg></div>
  </div>
  <div class="header-rule"></div>

  <div class="letter-content">
    <div class="letter-date">10 December, 2020</div>
    <div class="recipient-name">ADRIAN HOLLOWAY</div>
    <div class="recipient-title">Cheif Executive Officer</div>

    <div class="letter-body">
      <p>Contrary to popular belief, Lorem Ipsum is not simply random text. It has roots in a piece of classical Latin literature from 45 BC, making it over 2000 years old. Daniel Arvent, a Latin professor at Westbrook College in Ohio, looked up one of the more obscure Latin words, consectetur.</p>
      <p>Lorem Ipsum comes from sections 1.10.32 and 1.10.33 of "de Finibus Bonorum et Malorum" (The Extremes of Good and Evil) by Marcus Velino, written in 45 BC. This book is a treatise on the theory of ethics, very popular during the Renaissance. The first line of Lorem Ipsum.</p>
      <p>The standard chunk of Lorem Ipsum used since the 1500s is reproduced below for those interested.</p>
    </div>
    <div class="sign-off">Best Regards</div>
    <div class="signature-area" role="img" aria-label="Handwritten signature of the sender"></div>
  </div>

  <div class="footer-rule"></div>
  <div class="footer-band"></div>
</section>

<section class="sheet card-front">
  <div class="brand"><span class="brand-square"></span>Korvex Systems</div>
  <div class="card-divider"></div>
  <div class="card-details">
    <div class="card-name">MARCUS DELANEY</div>
    <div class="card-role">Founder &amp; CEO</div>
    <div class="card-address">1234 First Line Address<br>5678 Second Line Address</div>
    <div class="card-contact">
      <svg viewBox="0 0 10 10"><path d="M2 1 L4 1 L4.6 3.2 L3.4 4.2 Q4.5 6 5.8 6.6 L6.8 5.4 L9 6 L9 8 Q8.5 9 7.5 9 Q1 8 1 2.5 Q1 1.5 2 1 Z" fill="var(--ink)"/></svg>(555) 014-2290</div>
    <div class="card-contact">
      <svg viewBox="0 0 10 10"><rect x="0.5" y="2" width="9" height="6.5" fill="var(--ink)"/></svg>contact@korvexsystems.com</div>
    <div class="card-contact">
      <svg viewBox="0 0 10 10"><circle cx="5" cy="5" r="4.5" fill="var(--ink-muted)"/></svg>www.korvexsystems.com</div>
  </div>
</section>

<section class="sheet card-back">
  <div class="brand"><span class="brand-square"></span>Korvex Systems</div>
</section>

<section class="sheet envelope-back">
  <svg class="envelope-flap" viewBox="0 0 451 67" aria-hidden="true">
    <path d="M1 0 Q5 40 12 50 Q22 66 42 66 H409 Q429 66 439 50 Q446 40 450 0" fill="none" stroke="#d6d6d6" stroke-width="1"/>
  </svg>
  <div class="brand"><span class="brand-square"></span>Korvex Systems</div>
</section>

<section class="sheet envelope-front">
  <div class="brand"><span class="brand-square"></span>Korvex Systems</div>
  <div class="brand-ghost">Korvex Systems</div>
  <div class="return-address">1234 First Line Address<br>5678 Second Line Address</div>
</section>

</body>
</html>
```